Remodel Flyer for realtors

"T" Ridgeline Builders

4"x 9" rack card front and back

www.BrambleworkHomes.example

555-318-4726

Let us fix what your home inspector finds!

Send us your inspection summary.

We are a licensed and Insured contractor.
CRC8071943

Serving
Keller County and Pelham Hollow

This flyer will sit in realtor offices for realtors to give to there buyers and sellers.

Target Market(s)

Realtors

Industry/Entity Type

Construction

Colors

Designer to choose colors to be used in the design.

```html
<!DOCTYPE html>
<html lang="en">
<head>
<meta charset="utf-8">
<title>T Ridgeline Builders – Rack Card</title>
<link href="https://fonts.googleapis.com/css2?family=Roboto:wght@700&display=swap" rel="stylesheet">
<style>
  :root {
    --orange: #ee9427;
    --charcoal: #59595b;
    --ink: #4a4a4c;
    --paper: #f1f1f1;
    --cream: #f3e8d7;
    --mist: #e2e2e2;
    --stage: #ececec;
  }
  html, body {
    margin: 0;
    width: 1200px;
    height: 1000px;
    overflow: hidden;
    background: var(--stage);
    font-family: "Roboto", Arial, sans-serif;
  }
  .canvas { position: relative; width: 1200px; height: 1000px; }
  .rack-card {
    position: absolute;
    top: 143px;
    width: 314px;
    height: 710px;
    overflow: hidden;
  }
  .rack-card svg.card-shapes { position: absolute; inset: 0; }
  .card-front { left: 276px; background: var(--orange); }
  .card-back { left: 624px; background: var(--cream); }

  .brand {
    position: absolute;
    left: 0; right: 0;
    top: 262px;
    text-align: center;
    color: var(--ink);
    font-weight: 700;
  }
  .brand-mark {
    width: 100px; height: 100px;
    margin: 0 auto 30px;
    background: var(--orange);
  }
  .brand-name { font-size: 30px; letter-spacing: 2px; line-height: 1; }
  .brand-sub { font-size: 18px; letter-spacing: 12px; margin-top: 12px; padding-left: 12px; line-height: 1; }

  .info-item {
    position: absolute;
    left: 0; right: 0;
    text-align: center;
    color: var(--ink);
    font-weight: 700;
    font-size: 14.5px;
    line-height: 19px;
  }
  .info-item svg { display: block; margin: 0 auto 14px; }
  .info-item p { margin: 0; }
  .back-mark {
    display: block;
    width: 48px; height: 48px;
    margin: 0 auto 12px;
    border-radius: 50%;
    background: var(--orange);
  }
</style>
</head>
<body>
<main class="canvas">

  <!-- Front -->
  <section class="rack-card card-front">
    <svg class="card-shapes" width="314" height="710" viewBox="0 0 314 710">
      <polygon points="0,236 314,62 314,472 0,646" fill="#ffffff"/>
      <polygon points="0,242 314,68 314,467 0,637" fill="var(--paper)"/>
      <polygon points="164,154 314,72 314,242" fill="var(--charcoal)"/>
      <polygon points="0,467 0,637 151,552" fill="var(--charcoal)"/>
    </svg>
    <div class="brand">
      <div class="brand-mark"></div>
      <div class="brand-name">T RIDGELINE</div>
      <div class="brand-sub">BUILDERS</div>
    </div>
  </section>

  <!-- Back -->
  <section class="rack-card card-back">
    <svg class="card-shapes" width="314" height="710" viewBox="0 0 314 710">
      <polygon points="0,72 314,242 314,637 0,467" fill="var(--paper)"/>
      <polygon points="0,72 0,242 150,155" fill="var(--mist)"/>
      <polygon points="314,467 314,637 164,552" fill="var(--mist)"/>
    </svg>

    <div class="info-item" style="top:50px">
      <svg width="48" height="48" viewBox="0 0 48 48" aria-hidden="true">
        <g fill="var(--orange)">
          <circle cx="24" cy="24" r="16"/>
          <rect x="21" y="3" width="6" height="8"/><rect x="21" y="37" width="6" height="8"/>
          <rect x="3" y="21" width="8" height="6"/><rect x="37" y="21" width="8" height="6"/>
          <rect x="21" y="3" width="6" height="8" transform="rotate(45 24 24)"/>
          <rect x="21" y="37" width="6" height="8" transform="rotate(45 24 24)"/>
          <rect x="3" y="21" width="8" height="6" transform="rotate(45 24 24)"/>
          <rect x="37" y="21" width="8" height="6" transform="rotate(45 24 24)"/>
        </g>
        <circle cx="24" cy="24" r="11" fill="var(--cream)"/>
      </svg>
      <p>Let Us Fix<br>What Your Home Inspector Finds!</p>
    </div>

    <div class="info-item" style="top:180px">
      <svg width="32" height="44" viewBox="0 0 32 44" aria-hidden="true">
        <rect x="2" y="2" width="28" height="40" rx="3" fill="none" stroke="var(--orange)" stroke-width="3"/>
        <g stroke="var(--orange)" stroke-width="2.5">
          <line x1="8" y1="12" x2="24" y2="12"/><line x1="8" y1="18" x2="24" y2="18"/>
          <line x1="8" y1="24" x2="24" y2="24"/><line x1="8" y1="30" x2="24" y2="30"/>
        </g>
      </svg>
      <p>Send Us Your<br>Inspection Summary.</p>
    </div>

    <div class="info-item" style="top:314px">
      <svg width="46" height="46" viewBox="0 0 46 46" aria-hidden="true">
        <circle cx="23" cy="23" r="23" fill="var(--orange)"/>
        <circle cx="23" cy="18" r="6" fill="#fff"/>
        <path d="M13 33 q0 -8 10 -8 q10 0 10 8 z" fill="#fff"/>
      </svg>
      <p>Serving Keller County<br>and Pelham Hollow</p>
    </div>

    <div class="info-item" style="top:444px">
      <svg width="42" height="42" viewBox="0 0 42 42" aria-hidden="true">
        <g fill="none" stroke="var(--orange)" stroke-width="2.5">
          <circle cx="21" cy="21" r="18"/>
          <ellipse cx="21" cy="21" rx="8" ry="18"/>
          <line x1="21" y1="3" x2="21" y2="39"/>
          <line x1="3" y1="21" x2="39" y2="21"/>
          <path d="M6 12 h30 M6 30 h30"/>
        </g>
      </svg>
      <p>555-318-4726<br>www.BrambleworkHomes.example</p>
    </div>

    <div class="info-item" style="top:578px">
      <span class="back-mark"></span>
      <p>We are a licensed and Insured contractor.<br>CRC8071943</p>
    </div>
  </section>

</main>
</body>
</html>
```